Creative Stationary for Solo Law Firm

I am looking for stationary designs for my solo law firm called TM Halvorsen Law PLLC. My logo is attached. I'd like the logo incorporated into the design.

I'm looking for a stationary design that is a bit outside of the box and not too standard or boring. The final design should communicate professionalism.

Target Market(s)

United States Clients, Opposing Counsel

Industry/Entity Type

Legal

Font styles to use
Sans Serif

Requirements
Must have
• The stationary design must incorporate my logo design attached. The design itself must be creative. The envelope design must follow standard United States designs with room for the postage stamp at the top right corner and space for the recipient's address in the middle.

```html
<!DOCTYPE html>
<html lang="en">
<head>
<meta charset="utf-8">
<title>TM Halvorsen Law – Stationery Set</title>
<link href="https://fonts.googleapis.com/css2?family=Questrial&display=swap" rel="stylesheet">
<style>
  :root {
    --backdrop: #cfcfcf;
    --folder: #979797;
    --folder-edge: #8a8a8a;
    --paper: #f1f1f1;
    --navy: #0d2160;
    --ink: #2b2b2b;
    --band-gray: #c4c4c4;
  }
  * { box-sizing: border-box; margin: 0; padding: 0; }
  html, body { width: 1200px; height: 1041px; overflow: hidden; }
  body {
    background: var(--backdrop);
    font-family: "Questrial", "Century Gothic", sans-serif;
    color: var(--ink);
    position: relative;
  }
  .piece {
    position: absolute;
    background: var(--paper);
    box-shadow: 0 1px 3px rgba(0,0,0,.22);
    overflow: hidden;
  }
  .brand-name {
    font-family: "Questrial", sans-serif;
    color: var(--navy);
    text-transform: uppercase;
    letter-spacing: .02em;
    white-space: nowrap;
    position: absolute;
  }
  .accent-band {
    position: absolute; left: 0; bottom: 0; width: 100%;
    background: linear-gradient(90deg, var(--band-gray) 0%, #d6d6d6 35%, #5a6a99 65%, var(--navy) 85%, var(--band-gray) 100%);
  }

  /* Folder */
  .folder {
    left: 166px; top: 76px; width: 417px; height: 542px;
    background: var(--folder); border-radius: 3px;
  }
  .folder-spine {
    position: absolute; left: 0; top: 0; bottom: 0; width: 27px;
    border-right: 2px solid var(--folder-edge);
  }
  .folder-spine::after {
    content: ""; position: absolute; left: 23px; top: 0; bottom: 0;
    border-left: 1px solid var(--folder-edge);
  }
  .folder .brand-name { left: 0; width: 416px; text-align: center; top: 80px; font-size: 17.5px; }

  /* Letterhead */
  .letterhead { left: 615px; top: 94px; width: 403px; height: 523px; }
  .letterhead .brand-name { left: 37px; top: 44px; font-size: 11.5px; }
  .contact { position: absolute; font-size: 5.6px; line-height: 7.2px; color: #444; }
  .contact li { list-style: none; display: flex; align-items: center; gap: 3px; }
  .contact .icon { width: 5px; height: 5px; background: var(--navy); border-radius: 1px; display: inline-block; }
  .contact .address { margin-top: 3px; }
  .letterhead .contact { left: 295px; top: 34px; }
  .letter-body {
    position: absolute; left: 37px; top: 145px; width: 330px;
    font-size: 5.6px; line-height: 7.1px; text-align: justify;
  }
  .letter-body .salutation { font-weight: bold; margin-bottom: 8px; }
  .letter-body p { margin-bottom: 7px; }
  .sign-off { position: absolute; left: 37px; top: 318px; font-size: 5.6px; line-height: 7.2px; }
  .sign-off strong { display: block; }
  .signature {
    position: absolute; left: 84px; top: 312px; width: 82px; height: 32px;
    background: linear-gradient(90deg, rgba(143,160,214,.25), rgba(143,160,214,.45), rgba(143,160,214,.2));
    border-radius: 16px;
  }
  .letterhead .accent-band { height: 14px; }

  /* Envelopes */
  .envelope-front { left: 132px; top: 646px; width: 451px; height: 195px; }
  .envelope-front .brand-name { left: 24px; top: 32px; font-size: 11.5px; }
  .envelope-front .return-address { position: absolute; left: 24px; top: 58px; font-size: 5.6px; line-height: 7.2px; }
  .envelope-front .accent-band { height: 14px; }
  .envelope-back { left: 615px; top: 646px; width: 451px; height: 195px; }
  .envelope-flap { position: absolute; left: 0; top: 0; width: 100%; height: 66px; }
  .envelope-back .brand-name { left: 0; right: 0; text-align: center; top: 32px; font-size: 8.2px; }
  .envelope-back .web { position: absolute; left: 0; right: 0; bottom: 20px; text-align: center; font-size: 5.6px; }

  /* Business cards */
  .card-back { left: 416px; top: 870px; width: 167px; height: 96px; background: var(--folder); }
  .card-back .brand-name { left: 0; right: 0; text-align: center; top: 43px; font-size: 9.5px; }
  .card-front { left: 615px; top: 870px; width: 167px; height: 96px; }
  .card-front .brand-name { left: 16px; top: 43px; font-size: 6.2px; }
  .card-front .divider { position: absolute; left: 91px; top: 22px; height: 46px; border-left: 1px solid #d0d0d0; }
  .card-front .person { position: absolute; left: 98px; top: 22px; font-size: 4.4px; line-height: 5.4px; }
  .card-front .person-name { color: var(--navy); font-weight: bold; font-size: 5px; text-transform: uppercase; }
  .card-front .contact { position: relative; font-size: 4.2px; line-height: 5.4px; margin-top: 2px; }
  .card-front .contact .icon { width: 3.6px; height: 3.6px; }
  .card-front .accent-band { height: 7px; }
</style>
</head>
<body>

<section class="piece folder" aria-label="Presentation folder">
  <div class="folder-spine"></div>
  <div class="brand-name">TM Halvorsen Law</div>
</section>

<section class="piece letterhead" aria-label="Letterhead">
  <div class="brand-name">TM Halvorsen Law</div>
  <ul class="contact">
    <li><span class="icon"></span>555.210.4187</li>
    <li><span class="icon"></span>info@tmhalvorsenlaw.com</li>
    <li><span class="icon"></span>www.tmhalvorsenlaw.com</li>
    <li class="address">418 W. Harlan Ave, Suite B<br>Fairmont CA 90214</li>
  </ul>
  <div class="letter-body">
    <p class="salutation">Dear sir,</p>
    <p>Communication is a very integral part of living creatures, animals and humans. Communication may be verbal or written. Written communication however is only applicable to human beings. Can you even imagine a world without communication? Verbal communication can be through telephones, webcams or in person. Written communication is through letters, emails and mobile phone messages.</p>
    <p>In today's world of great inventions and technology, letters have somehow become redundant. It is the time for text messages or chats. But they still can communicate a lot more than all other modes of communication. Organizations and various government departments still bank on letters as a strong medium of communication. There is no comparison in costs of sending letters as compared to costs of mobile phone messages though – letters are far cheaper. Letters now commonly known as "hard copy documents" are considered more relevant and important than email copies of text messages as proof or evidence of some sort.</p>
    <p>Letters speak volumes about a person or an organization that writes it. So one must take utmost care ensuring that the language used in any letter is appropriate for the occasion for which it is being written. Since a letter is also a written proof or document, if there are certain things that should not form a part of it, then that too should be carefully handled.</p>
    <p>Writing a good letter is an art. But if for some reason someone is unable to write that perfect letter, these different types of letters provide a base for you to build on. Sample letters have been given for everyone to understand what all information needs to form a part of the letter type and then it can be customized.</p>
  </div>
  <div class="sign-off">Yours Sincerely,<strong>Dana Whitcomb</strong></div>
  <div class="signature" role="img" aria-label="Handwritten signature of the sender"></div>
  <div class="accent-band" role="img" aria-label="Decorative gray and navy wave band"></div>
</section>

<section class="piece envelope-front" aria-label="Envelope front">
  <div class="brand-name">TM Halvorsen Law</div>
  <div class="return-address">418 W. Harlan Ave, Suite B<br>Fairmont CA 90214</div>
  <div class="accent-band" role="img" aria-label="Decorative gray and navy wave band"></div>
</section>

<section class="piece envelope-back" aria-label="Envelope back">
  <svg class="envelope-flap" viewBox="0 0 451 66" preserveAspectRatio="none" aria-hidden="true">
    <path d="M0 0 H451 L434 58 Q432 63 426 63 H25 Q19 63 17 58 Z" fill="var(--folder)"/>
  </svg>
  <div class="brand-name">TM Halvorsen Law</div>
  <div class="web">www.tmhalvorsenlaw.com</div>
</section>

<section class="piece card-back" aria-label="Business card back">
  <div class="brand-name">TM Halvorsen Law</div>
</section>

<section class="piece card-front" aria-label="Business card front">
  <div class="brand-name">TM Halvorsen Law</div>
  <div class="divider"></div>
  <div class="person">
    <div class="person-name">Jordan Ellery</div>
    <div>General Manager</div>
    <ul class="contact">
      <li><span class="icon"></span>555.210.4187</li>
      <li><span class="icon"></span>info@tmhalvorsenlaw.com</li>
      <li><span class="icon"></span>www.tmhalvorsenlaw.com</li>
      <li class="address">418 W. Harlan Ave, Suite B<br>Fairmont CA 90214</li>
    </ul>
  </div>
  <div class="accent-band" role="img" aria-label="Decorative gray and navy wave band"></div>
</section>

</body>
</html>
```